FULLY CUSTOM MAIN BANNER IMAGE FOR MY WEBSITE-REDESIGN CURRENT

SIZE MUST BE: 1800x829

LOOKING FOR A FULLY CUSTOM MAIN BANNER IMAGE TO BE DESIGNED FOR MY NEW WEBSITE HOMEPAGE http://gridplankstudio.com/dh/derek/vtr_final/index.html THE CONTENT THAT YOU SEE ON THE UPLOADED FILE OR HERE http://gridplankstudio.com/dh/derek/vtr_final/index.html YOU CAN SEE MY EXISTING BANNER IMAGE...IS THE SAME CONTENT I WANT ON THE CUSTOM BANNER IMAGE BUT I WANT THE BANNER IMAGE TO USE IMAGES TO PORTRAY WHAT THE CONTENT SAYS. POSSIBLE INTEGRATE AN INFOGRAPHIC DESIGN IN THE BANNER IMAGE. IM OPEN TO ALL IDEAS.

WHEN SOMEONE GOES TO MY WEBSITE, IMMEDIATELY I WANT THEM TO UNDERSTAND WHAT IT IS I DO.

MY BUSINESS PROVIDES OTHER BUSINESSES WITH THE ABILITY TO CREATE PROMOTIONAL GIVEAWAYS AND MARKETING PROMOTIONS USING GIFT VOUCHERS THAT ARE REDEEMABLE FOR FREE VACATIONS, CRUISES, ALL INCLUSIVE RESORT STAYS, TABLETS, SMARTWATCHES, DINING AND RESTAURANT INCENTIVES AND REWARDS AND MORE.

CURRENTLY THE CONTENT ON THE BANNER IMAGE IS THIS:
BOOST SALES & LEADS OVERNIGHT
BY ENTICING YOUR CUSTOMERS WITH FREE VACATION CERTIFICATES & OTHER HIGH PERCEIVED VALUE INCENTIVES

I HAVE ATTACHED A DOCUMENT WITH IMAGE ASSETTS YOU MAY REVIEW AND USE OR GET IDEAS FROM.

THE BOTTOM LINE IS MY SERVICE HELPS BUSINESSES INCREASE LEADS, CONVERSIONS, CTA, SALES, ETC WITHOUT HAVING TO INCREASE THEIR EXISTING AD SPEND. SIMPLY BY ADDING A FREE OFFER TO ALL THEIR EXISTING ADS WILL DRAMATICALLY INCREASE RESPONSE RATES. SO I WANT THIS BANNER TO REFLECT THIS SOMEHOW....MORE CUSTOMERS USING GIVEAWAYS!

Target Market(s)

B2B, SMALL BUSINESS OWNERS, ENTREPRENEURS, SOLOPRENEURS, MARKETING AGENCIES,

Industry/Entity Type

Digital Marketing

Requirements
Must have
• MUST PORTRAY THE RED CONTENT/TEXT USING IMAGES OF MY ASSETTS AND THE PORTRAY MORE CUSTOMERS---MUST BE FULLY CUSTOM

SIZE MUST BE: 1800x829
Nice to have
• USE CONTENT IN CURRENT BANNER IMAGE ALSO MAKE SURE TO USE THE FREE SAMPLE PKG BUTTON TOO.....MUST BE FULLY CUSTOM

SIZE MUST BE: 1800x829
Should not have
• MUST BE FULLY CUSTOM

SIZE MUST BE: 1800x829

```html
<!DOCTYPE html>
<html lang="en">
<head>
<meta charset="utf-8">
<title>Voucher Trail Rewards – Homepage Banner</title>
<link href="https://fonts.googleapis.com/css2?family=Montserrat:wght@400;500;600;700&family=Orbitron:wght@700;900&display=swap" rel="stylesheet">
<style>
:root{
  --stage:#4a97c2;
  --brand-blue:#1a6fc0;
  --nav-blue:#1c6fbf;
  --deep-blue:#0f5aa8;
  --brand-green:#3fae49;
  --btn-green:#43ad4c;
  --charcoal:#3b3f45;
  --ink:#222;
  --hero-light:#f3f3f3;
  --hero-mid:#d6d6d6;
  --divider:#e2e2e2;
  --white:#fff;
}
*{margin:0;padding:0;box-sizing:border-box}
html,body{width:1200px;height:2208px;overflow:hidden}
body{background:var(--stage);font-family:'Montserrat',sans-serif;position:relative}

.banner{position:absolute;width:1300px;transform-origin:0 0;box-shadow:0 8px 18px rgba(0,0,0,.25);background:var(--white)}
.banner--desktop{left:151px;top:141px;transform:scale(.692)}
.banner--wide{left:48px;top:867px;transform:scale(.85)}
.banner--full{left:43px;top:1526px;transform:scale(.857)}

/* top bar */
.topbar{position:relative;height:74px;background:var(--nav-blue);display:flex}
.topbar__brand{position:absolute;left:0;top:0;height:74px;width:420px}
.topbar__brand svg{position:absolute;left:0;top:0}
.brand-name{position:absolute;left:28px;top:24px;display:flex;align-items:center;gap:10px;color:var(--brand-blue);font-weight:700;font-size:21px;letter-spacing:.3px;white-space:nowrap}
.brand-name i{display:block;width:18px;height:18px;background:var(--brand-blue)}
.nav{position:absolute;left:400px;top:0;width:576px;height:74px;display:flex;align-items:center;white-space:nowrap}
.nav a{color:var(--white);font-weight:600;font-size:13px;text-decoration:none;padding:0 7px;border-left:1px solid rgba(255,255,255,.35);line-height:16px;white-space:nowrap}
.nav a:first-child{border-left:0}
.account{position:absolute;top:0;height:74px;width:76px;display:flex;flex-direction:column;align-items:center;justify-content:center;color:var(--white);font-size:12px;gap:4px}
.account--login{left:980px;background:var(--charcoal)}
.account--signup{left:1056px;background:var(--nav-blue)}
.office{position:absolute;left:1132px;top:0;width:168px;height:74px;background:var(--brand-green);color:var(--white);display:flex;align-items:center;padding-left:10px;gap:8px;white-space:nowrap}
.office small{display:block;font-size:13px}
.office b{display:block;font-weight:500;font-size:17px;letter-spacing:.2px;white-space:nowrap}

/* hero */
.hero{position:relative;height:600px;overflow:hidden;background:linear-gradient(115deg,var(--hero-light) 0%,#ebebeb 40%,var(--hero-mid) 70%,#c9c9c9 100%)}
.banner--wide .hero{background:linear-gradient(115deg,#d9d9d9 0%,#ececec 40%,#d4d4d4 75%,#c2c2c2 100%)}
.hero__glow{position:absolute;inset:0}
.hero__headline{position:absolute;left:0;top:70px}
.hero__tagline{position:absolute;left:0;right:0;top:168px;text-align:center;font-size:20px;font-weight:500;color:var(--ink);letter-spacing:.1px;white-space:nowrap}
.hero__samples{position:absolute;left:293px;top:206px;width:712px;height:218px;background:linear-gradient(90deg,#1d2431 0%,#1f6d35 14%,#c9235f 22%,#e9e3dc 30%,#1c3d66 45%,#2d86a8 58%,#e8e4e0 70%,#d12a2a 78%,#2a80b6 85%,#d9b49a 93%,#c79a7d 100%);box-shadow:0 6px 10px rgba(0,0,0,.35)}
.hero__limited{position:absolute;left:0;right:0;top:440px;text-align:center;font-family:'Orbitron',sans-serif;font-weight:700;font-size:22px;color:var(--brand-blue);letter-spacing:.5px;white-space:nowrap}
.hero__limited em{font-style:normal;color:var(--brand-green)}
.cta{position:absolute;left:462px;top:482px;width:376px;height:80px;border-radius:8px;background:var(--btn-green);box-shadow:0 6px 8px rgba(0,0,0,.2);color:var(--white);text-align:center;padding-top:10px;white-space:nowrap}
.cta__main{display:block;font-family:'Orbitron',sans-serif;font-weight:900;font-size:28px;letter-spacing:.5px}
.cta__sub{display:block;font-weight:700;font-size:21px;margin-top:2px}
.corner{position:absolute}

/* stats */
.stats{height:136px;background:var(--white);display:flex;padding-left:190px}
.stat{width:157px;display:flex;flex-direction:column;align-items:center;padding-top:38px;border-right:1px solid var(--divider)}
.stat:last-child{border-right:0}
.stat__value{font-size:29px;font-weight:500;color:var(--ink);margin-top:6px}
</style>
</head>
<body>

<section class="banner banner--desktop">
  <header class="topbar">
    <div class="topbar__brand">
      <svg width="420" height="74"><polygon points="0,0 355,0 395,74 0,74" fill="#fff"/></svg>
      <div class="brand-name"><i></i>Voucher Trail Rewards</div>
    </div>
    <nav class="nav"><a>Home</a><a>Our Incentives</a><a>Samples</a><a>Affiliates</a><a>Testimonials</a><a>Faq</a><a>Contact Us</a></nav>
    <div class="account account--login"><svg width="18" height="18" viewBox="0 0 18 18"><circle cx="9" cy="5" r="4" fill="#fff"/><path d="M1 18c0-5 4-7 8-7s8 2 8 7z" fill="#fff"/></svg>LOGIN</div>
    <div class="account account--signup"><svg width="18" height="18" viewBox="0 0 18 18"><circle cx="9" cy="9" r="8" fill="none" stroke="#fff" stroke-width="1.6"/><path d="M9 13V5M5.5 8.5 9 5l3.5 3.5" fill="none" stroke="#fff" stroke-width="1.8"/></svg>SIGN UP</div>
    <div class="office"><svg width="20" height="36" viewBox="0 0 20 36"><rect x="1.5" y="1.5" width="17" height="33" rx="3" fill="none" stroke="#fff" stroke-width="2.5"/><rect x="7" y="29" width="6" height="2" fill="#fff"/></svg><div><small>USA Office :</small><b>555-014-2290</b></div></div>
  </header>
  <div class="hero">
    <svg class="hero__glow" width="1300" height="600"><polygon points="820,600 1000,0 1300,0 1300,600" fill="rgba(255,255,255,.25)"/><polyline points="930,420 1050,300 1150,380 1300,180" fill="none" stroke="rgba(255,255,255,.8)" stroke-width="5"/></svg>
    <svg class="corner" style="left:1167px;top:0" width="133" height="140"><polygon points="0,0 133,0 133,20 65,135" fill="var(--brand-blue)"/></svg>
    <svg class="corner" style="left:0;top:460px" width="130" height="140"><polygon points="0,140 130,140 68,0" fill="var(--brand-blue)"/></svg>
    <svg class="hero__headline" width="1300" height="90" viewBox="0 0 1300 90">
      <text x="133" y="55" font-family="Orbitron, sans-serif" font-weight="900" font-size="60" textLength="230" lengthAdjust="spacingAndGlyphs" fill="var(--brand-green)">BOOST</text>
      <text x="388" y="55" font-family="Orbitron, sans-serif" font-weight="900" font-size="52" textLength="450" lengthAdjust="spacingAndGlyphs" fill="var(--charcoal)">SALES &amp; LEADS</text>
      <text x="858" y="55" font-family="Orbitron, sans-serif" font-weight="900" font-size="54" textLength="307" lengthAdjust="spacingAndGlyphs" fill="var(--brand-blue)">OVERNIGHT</text>
      <rect x="158" y="64" width="1008" height="3" fill="var(--charcoal)"/>
    </svg>
    <p class="hero__tagline">BY ENTICING YOUR CUSTOMERS WITH FREEVACATION CERTIFICATES &amp; OTHER HIGHPERCEIVED VALUE INCENTIVES</p>
    <div class="hero__samples" role="img" aria-label="Fanned row of sample vacation certificate and free gift voucher flyers"></div>
    <p class="hero__limited">GET <em>FREE</em> SAMPLES NOW FOR A LIMITED TIME !</p>
    <a class="cta"><span class="cta__main">GET FREE SAMPLES</span><span class="cta__sub">100% FREE</span></a>
  </div>
  <div class="stats">
    <div class="stat"><svg width="46" height="50" viewBox="0 0 46 50" fill="none" stroke="var(--brand-blue)" stroke-width="2.5"><rect x="4" y="34" width="7" height="14"/><rect x="15" y="26" width="7" height="22"/><rect x="26" y="18" width="7" height="30"/><rect x="37" y="10" width="7" height="38"/><path d="M3 26 20 12l8 6 15-15M36 3h7v7" stroke="var(--brand-green)"/></svg><span class="stat__value">0+</span></div>
    <div class="stat"><svg width="66" height="44" viewBox="0 0 66 44" fill="none" stroke="var(--brand-blue)" stroke-width="2.5"><circle cx="14" cy="10" r="7"/><circle cx="33" cy="10" r="7"/><circle cx="52" cy="10" r="7"/><path d="M2 40c0-12 24-12 24 0M21 40c0-12 24-12 24 0M40 40c0-12 24-12 24 0" stroke="var(--brand-green)"/></svg><span class="stat__value">0+</span></div>
    <div class="stat"><svg width="54" height="50" viewBox="0 0 54 50" fill="none" stroke="var(--brand-green)" stroke-width="2.5"><rect x="2" y="2" width="50" height="38" rx="2"/><circle cx="33" cy="26" r="9" stroke="var(--brand-blue)"/><path d="M29 34l-3 14 7-4 7 4-3-14" stroke="var(--brand-blue)"/></svg><span class="stat__value">0+</span></div>
    <div class="stat"><svg width="46" height="50" viewBox="0 0 46 50" fill="none" stroke="var(--brand-blue)" stroke-width="2.5"><rect x="4" y="20" width="38" height="28"/><rect x="2" y="13" width="42" height="8" stroke="var(--brand-green)"/><path d="M23 13v35M23 13c-6-10-14-6-9 0M23 13c6-10 14-6 9 0" stroke="var(--brand-green)"/></svg><span class="stat__value">0+</span></div>
    <div class="stat"><svg width="46" height="50" viewBox="0 0 46 50" fill="none" stroke="var(--brand-blue)" stroke-width="2.5"><rect x="3" y="22" width="9" height="24" stroke="var(--brand-green)"/><path d="M12 24l10-14 2-8c5 0 6 6 4 14h13c3 0 4 3 3 6l-4 20H12z"/></svg><span class="stat__value">Top</span></div>
    <div class="stat"><svg width="48" height="50" viewBox="0 0 48 50" fill="none" stroke="var(--brand-green)" stroke-width="2.5"><path d="M6 44 20 30M4 34l10 10M14 24l10 10"/><rect x="20" y="6" width="20" height="24" stroke="var(--brand-blue)"/><circle cx="40" cy="8" r="6" stroke="var(--brand-blue)"/></svg><span class="stat__value">0</span></div>
  </div>
</section>

<section class="banner banner--wide">
  <header class="topbar">
    <div class="topbar__brand">
      <svg width="420" height="74"><polygon points="0,0 355,0 395,74 0,74" fill="#fff"/></svg>
      <div class="brand-name"><i></i>Voucher Trail Rewards</div>
    </div>
    <nav class="nav"><a>Home</a><a>Our Incentives</a><a>Samples</a><a>Affiliates</a><a>Testimonials</a><a>Faq</a><a>Contact Us</a></nav>
    <div class="account account--login"><svg width="18" height="18" viewBox="0 0 18 18"><circle cx="9" cy="5" r="4" fill="#fff"/><path d="M1 18c0-5 4-7 8-7s8 2 8 7z" fill="#fff"/></svg>LOGIN</div>
    <div class="account account--signup"><svg width="18" height="18" viewBox="0 0 18 18"><circle cx="9" cy="9" r="8" fill="none" stroke="#fff" stroke-width="1.6"/><path d="M9 13V5M5.5 8.5 9 5l3.5 3.5" fill="none" stroke="#fff" stroke-width="1.8"/></svg>SIGN UP</div>
    <div class="office"><svg width="20" height="36" viewBox="0 0 20 36"><rect x="1.5" y="1.5" width="17" height="33" rx="3" fill="none" stroke="#fff" stroke-width="2.5"/><rect x="7" y="29" width="6" height="2" fill="#fff"/></svg><div><small>USA Office :</small><b>555-014-2290</b></div></div>
  </header>
  <div class="hero" role="img" aria-label="Faded banknote texture behind the headline">
    <svg class="hero__glow" width="1300" height="600"><polygon points="820,600 1000,0 1300,0 1300,600" fill="rgba(255,255,255,.2)"/><polygon points="0,0 260,0 60,600 0,600" fill="rgba(180,180,180,.25)"/></svg>
    <svg class="corner" style="left:1167px;top:0" width="133" height="140"><polygon points="0,0 133,0 133,20 65,135" fill="var(--brand-blue)"/></svg>
    <svg class="hero__headline" width="1300" height="90" viewBox="0 0 1300 90">
      <text x="133" y="55" font-family="Orbitron, sans-serif" font-weight="900" font-size="60" textLength="230" lengthAdjust="spacingAndGlyphs" fill="var(--brand-green)">BOOST</text>
      <text x="388" y="55" font-family="Orbitron, sans-serif" font-weight="900" font-size="52" textLength="450" lengthAdjust="spacingAndGlyphs" fill="var(--charcoal)">SALES &amp; LEADS</text>
      <text x="858" y="55" font-family="Orbitron, sans-serif" font-weight="900" font-size="54" textLength="307" lengthAdjust="spacingAndGlyphs" fill="var(--brand-blue)">OVERNIGHT</text>
      <rect x="158" y="64" width="1008" height="3" fill="var(--charcoal)"/>
    </svg>
    <p class="hero__tagline">BY ENTICING YOUR CUSTOMERS WITH FREEVACATION CERTIFICATES &amp; OTHER HIGHPERCEIVED VALUE INCENTIVES</p>
    <div class="hero__samples" role="img" aria-label="Fanned row of sample vacation certificate and free gift voucher flyers"></div>
    <p class="hero__limited">GET <em>FREE</em> SAMPLES NOW FOR A LIMITED TIME !</p>
    <a class="cta"><span class="cta__main">GET FREE SAMPLES</span><span class="cta__sub">100% FREE</span></a>
  </div>
</section>

<section class="banner banner--full">
  <header class="topbar">
    <div class="topbar__brand">
      <svg width="420" height="74"><polygon points="0,0 355,0 395,74 0,74" fill="#fff"/></svg>
      <div class="brand-name"><i></i>Voucher Trail Rewards</div>
    </div>
    <nav class="nav"><a>Home</a><a>Our Incentives</a><a>Samples</a><a>Affiliates</a><a>Testimonials</a><a>Faq</a><a>Contact Us</a></nav>
    <div class="account account--login"><svg width="18" height="18" viewBox="0 0 18 18"><circle cx="9" cy="5" r="4" fill="#fff"/><path d="M1 18c0-5 4-7 8-7s8 2 8 7z" fill="#fff"/></svg>LOGIN</div>
    <div class="account account--signup"><svg width="18" height="18" viewBox="0 0 18 18"><circle cx="9" cy="9" r="8" fill="none" stroke="#fff" stroke-width="1.6"/><path d="M9 13V5M5.5 8.5 9 5l3.5 3.5" fill="none" stroke="#fff" stroke-width="1.8"/></svg>SIGN UP</div>
    <div class="office"><svg width="20" height="36" viewBox="0 0 20 36"><rect x="1.5" y="1.5" width="17" height="33" rx="3" fill="none" stroke="#fff" stroke-width="2.5"/><rect x="7" y="29" width="6" height="2" fill="#fff"/></svg><div><small>USA Office :</small><b>555-014-2290</b></div></div>
  </header>
  <div class="hero">
    <svg class="hero__glow" width="1300" height="600"><polygon points="820,600 1000,0 1300,0 1300,600" fill="rgba(255,255,255,.25)"/><polyline points="930,420 1050,300 1150,380 1300,180" fill="none" stroke="rgba(255,255,255,.8)" stroke-width="5"/></svg>
    <svg class="corner" style="left:1167px;top:0" width="133" height="140"><polygon points="0,0 133,0 133,20 65,135" fill="var(--brand-blue)"/></svg>
    <svg class="corner" style="left:0;top:460px" width="130" height="140"><polygon points="0,140 130,140 68,0" fill="var(--brand-blue)"/></svg>
    <svg class="hero__headline" width="1300" height="90" viewBox="0 0 1300 90">
      <text x="133" y="55" font-family="Orbitron, sans-serif" font-weight="900" font-size="60" textLength="230" lengthAdjust="spacingAndGlyphs" fill="var(--brand-green)">BOOST</text>
      <text x="388" y="55" font-family="Orbitron, sans-serif" font-weight="900" font-size="52" textLength="450" lengthAdjust="spacingAndGlyphs" fill="var(--charcoal)">SALES &amp; LEADS</text>
      <text x="858" y="55" font-family="Orbitron, sans-serif" font-weight="900" font-size="54" textLength="307" lengthAdjust="spacingAndGlyphs" fill="var(--brand-blue)">OVERNIGHT</text>
      <rect x="158" y="64" width="1008" height="3" fill="var(--charcoal)"/>
    </svg>
    <p class="hero__tagline">BY ENTICING YOUR CUSTOMERS WITH FREEVACATION CERTIFICATES &amp; OTHER HIGHPERCEIVED VALUE INCENTIVES</p>
    <div class="hero__samples" role="img" aria-label="Fanned row of sample vacation certificate and free gift voucher flyers"></div>
    <p class="hero__limited">GET <em>FREE</em> SAMPLES NOW FOR A LIMITED TIME !</p>
    <a class="cta"><span class="cta__main">GET FREE SAMPLES</span><span class="cta__sub">100% FREE</span></a>
  </div>
</section>

</body>
</html>
```